Corvend Utility Services Ltd. -Website Design

We need a site design for a new company based in Toronto, Ontario called 'Corvend Utility Services Ltd.'

We provide Engineering services, Subsurface Utility Engineering services and Geospatial Data Management.

Our clients are typically Utilities (electric, gas, water/waste water, telcom) or contractors/consultants working on their behalf.

Our business model is new and we are the first to offer all three services to our clients; this allows us to provide value-added services from all three of our main offerings.

Target Market(s)

Field Supervisors, Managers, Directors, VP's at Utility companies

Industry/Entity Type

Business

Requirements
Must have
• -The landing page must clearly identify the 3 main business offerings allowing the user to easily navigate to each....Utility Engineering, GIS Data Management & Sub-surface Utility Engineering (SUE).

-Interactive contact page with integrated email

-based on existing logo design...
Nice to have
• -Ability to easily add/post news releases, updates, jobs, etc...

-Ability to integrate instructional YouTube video(s)

Should not have
• -Cannot be too cluttered....

```html
<!DOCTYPE html>
<html lang="en">
<head>
<meta charset="utf-8">
<title>Corvend Utility Services Ltd.</title>
<link href="https://fonts.googleapis.com/css2?family=Carlito:wght@400;700&display=swap" rel="stylesheet">
<style>
:root{
  --page:#141410;
  --header:#161612;
  --panel:#272727;
  --white:#ffffff;
  --accent:#eea012;
  --accent-dark:#c97f06;
  --heading:#6b9ac4;
  --bullet:#9bbbe0;
  --text:#222222;
  --divider:#3a3a3a;
  --muted:#6d6d6d;
  --label:#d8d8d8;
}
*{margin:0;padding:0;box-sizing:border-box}
html,body{width:942px;height:1200px;overflow:hidden;background:var(--page)}
body{position:relative;font-family:"Carlito",sans-serif;color:var(--text)}
.site-header{position:absolute;left:0;top:0;width:942px;height:108px;background:linear-gradient(#1c1c18,#111110)}
.brand{position:absolute;left:22px;top:34px;display:flex;align-items:center;gap:14px}
.brand-mark{width:30px;height:30px;background:var(--accent)}
.brand-name{color:var(--white);font-weight:700;font-size:42px;letter-spacing:3px;line-height:1}
.main-nav{position:absolute;top:47px;left:600px;display:flex;gap:8px}
.main-nav a{display:block;height:28px;line-height:28px;text-align:center;color:var(--white);text-decoration:none;font-size:17px;background:linear-gradient(#f4ae1c,var(--accent-dark));border:1px solid #b87205}
.main-nav a.is-active{color:#1a1a1a}
.nav-home{width:84px}.nav-services{width:103px}.nav-contact{width:121px}
.hero{position:absolute;left:18px;top:108px;width:906px;height:339px;background:linear-gradient(165deg,#0d1a2a 0%,#122a44 18%,#e8eef4 38%,#6fa6d6 58%,#1f6fbf 78%,#0a2246 100%)}
.offerings{position:absolute;left:18px;top:447px;width:906px;height:396px;background:var(--white);display:flex}
.offering{height:100%;padding:20px 0 0 16px}
.offering + .offering{border-left:1px solid var(--divider)}
.offering:nth-child(1){width:304px}
.offering:nth-child(2){width:302px}
.offering:nth-child(3){width:300px;padding-top:12px}
.offering h2{color:var(--heading);font-weight:400;font-size:21px;line-height:23px;letter-spacing:.6px;min-height:46px}
.offering:nth-child(3) h2{min-height:54px}
.offering ul{list-style:none;margin-top:7px}
.offering li{position:relative;padding-left:13px;font-size:13.5px;letter-spacing:.4px;line-height:18px;margin-bottom:8px}
.offering li::before{content:"";position:absolute;left:1px;top:6px;width:6px;height:6px;border-radius:50%;background:var(--bullet)}
.offering li.tight{margin-bottom:8px}
.offering:nth-child(2) li{margin-bottom:8px}
.lower-band{position:absolute;left:18px;top:843px;width:906px;height:285px;background:var(--panel)}
.video-player{position:absolute;left:23px;top:13px;width:437px;height:259px;background:#000}
.video-play{position:absolute;left:201px;top:110px}
.video-controls{position:absolute;left:0;bottom:0;width:100%;height:19px;background:linear-gradient(#f2f2f2,#bdbdbd);display:flex;align-items:center;font-size:9px;font-weight:700;color:#222;padding:0 6px;gap:8px}
.video-track{flex:1;height:5px;background:#9a9a9a;border-radius:2px}
.quick-contact{position:absolute;left:570px;top:17px;width:300px}
.quick-contact h2{color:var(--heading);font-weight:700;font-size:21px;letter-spacing:.8px;margin-bottom:20px}
.field{display:flex;margin-bottom:12px}
.field label{width:83px;padding-left:12px;color:var(--label);font-size:15px;letter-spacing:.5px;line-height:24px}
.field .input{width:191px;height:25px;background:var(--white);border:none}
.field .textarea{height:59px}
.submit{position:absolute;left:191px;top:232px;width:83px;height:23px;background:linear-gradient(#f4ae1c,var(--accent-dark));border:1px solid #b87205;color:#1a1a1a;font-family:inherit;font-size:15px}
.site-footer{position:absolute;left:0;top:1163px;width:942px;text-align:center;color:var(--muted);font-size:10px;letter-spacing:.3px}
</style>
</head>
<body>
<header class="site-header">
  <div class="brand"><span class="brand-mark"></span><span class="brand-name">CORVEND</span></div>
  <nav class="main-nav">
    <a class="nav-home is-active" href="#">Home</a>
    <a class="nav-services" href="#">Services</a>
    <a class="nav-contact" href="#">Contact Us</a>
  </nav>
</header>

<div class="hero" role="img" aria-label="View of Earth from orbit with cloud cover over blue ocean"></div>

<main class="offerings">
  <section class="offering">
    <h2>Utility Engineering</h2>
    <ul>
      <li>Project Management;</li>
      <li>Outside Plant Network Design;</li>
      <li>Utility Design and Permitting;</li>
      <li>Project Management;</li>
      <li>Surveys and Mapping (GPS);</li>
      <li>Pole line design and attachment permitting (Pole Load Calculations);</li>
      <li>Specialty Permits for the Utility Industry (Railway, Transport Ministry, Conservation Authority);</li>
      <li>Manhole and Duct Bank Design.</li>
    </ul>
  </section>
  <section class="offering">
    <h2>GIS Data Management</h2>
    <ul>
      <li>GIS Project Management;</li>
      <li>Records Conversion for GIS Systems;</li>
      <li>Landbase Data Management;</li>
      <li>Data Translation and Transformation</li>
      <li>Between File Formats;</li>
      <li>Hydro Asset Management using Geonix;</li>
      <li>Spatial Data Analysis &amp; Manipulation;</li>
      <li>Fibre Asset Management using Geonix &amp;</li>
      <li>LineGrid Software;</li>
      <li>Custom Cartographic Mapping;</li>
      <li>Engineering and Base Mapping using Geonix,</li>
      <li>DraftCore, MapLedger;</li>
    </ul>
  </section>
  <section class="offering">
    <h2>Sub-surface<br>Utility Engineering (SUE)</h2>
    <ul>
      <li>Project Management;</li>
      <li>Consulting;</li>
      <li>Surveying;</li>
      <li>CAD Processing of Results.</li>
    </ul>
  </section>
</main>

<section class="lower-band">
  <div class="video-player">
    <svg class="video-play" width="26" height="20" viewBox="0 0 26 20"><path d="M1 1 L25 10 L1 19 Z" fill="#fff"/></svg>
    <div class="video-controls">
      <span>&#9654;</span><span>00:01</span><span class="video-track"></span><span>100 %</span><span>&#9635;</span><span>&#9646;&#9646;&#9646;</span>
    </div>
  </div>
  <form class="quick-contact">
    <h2>Quick Contact</h2>
    <div class="field"><label>Name</label><span class="input"></span></div>
    <div class="field"><label>Email</label><span class="input"></span></div>
    <div class="field"><label>Phone</label><span class="input"></span></div>
    <div class="field"><label>Message</label><span class="input textarea"></span></div>
    <button class="submit" type="button">Submit</button>
  </form>
</section>

<footer class="site-footer">©2012 Corvend - Terms of Service - Privacy Policy - Program Policies</footer>
</body>
</html>
```